Fern Vale Ridgecrest Music Festival Poster

We are a summer music festival with concerts spanning Jazz, Cabaret, Education, Broadway, Chamber and Opera. We are looking for our key art for the 2016 season. This design will serve as the basis for all promotional materials, the concert program, and our web materials. Though eventually this means we will need to adjust the design to fit many different sizes, our poster will be printed mostly on 8.5" x 11" paper, and we can adapt from there. The design will be featured online and in print. It should be vertical and not landscape.

WE ARE SEEKING SLEEK, ELEGANT DESIGNS WITH MAYBE A KEY STOCK PHOTOGRAPH AND THE RELEVANT TEXT/DETAILS.

PLEASE NOTE: The included file "avenir logo.psd" is just a suggestion for the feel we are going for. It is our "working logo" after having scraped our old logo. We are interested in seeing your own ideas on how to style the brand name, but if you have ideas working with this version of the logo, feel free to use it.

REQUIRED DETAILS:
Festival Name: Fern Vale Ridgecrest Music Festival
Dates: July 29 - August 7 2016 (the year, 2016, must be included on the poster, but it does not need to be in the same location as where the actual dates are listed)
Website: www.fernvaleridgecrestfest.org

Additional Information:
- the 7 musical styles (jazz, choral, cabaret, education, broadway, chamber, opera) are important to defining who we are. You may decide to include these on the poster.
- We are looking for a very elegant design

TARGET:
We depend highly on an older clientele. We are working to expand our brand into younger demographics, but we want to be sure that we do not alienate our current consumer base with text that may be difficult for them to read.

Project Deadline Extended Reason: I am extending the deadline because it is taking longer to get feedback from my superiors than I had expected. Extending the deadline will give me time to provide adequate feedback from the people who will ultimately be making the decision. Thank you. Added Saturday, January 30, 2016

Sorry for the delay. There were issues with the decision makers but we are selecting in the next 24 hours.

Target Market(s)

Lovers of the styles of music we feature. We have a good number of elderly consumers, but also families and school groups (discussed further in description section)

Industry/Entity Type

Entertainment

Font styles to use
Sans Serif

Requirements
Must have
• Festival Name: Fern Vale Ridgecrest Music Festival
• Dates: July 29 - August 7 2016 (the year, 2016, must be included on the poster, but it does not need to be in the same location as where the actual dates are listed)
• Website: www.fernvaleridgecrestfest.org
Nice to have
• - the 7 musical styles (jazz, choral, cabaret, education, broadway, chamber, opera) are important to defining who we are. We would love to include these styles somewhere on the image, or feature them somehow in the artwork
• - Our brand has an elegance to it due to the type of music we offer, and our location being in a very natural space. inclusion of the music/nature mixed aspect of our brand in artwork might be nice
Should not have
• Anything that may offend or alienate an older, more conservative demographic

```html
<!DOCTYPE html>
<html lang="en">
<head>
<meta charset="utf-8">
<title>Fern Vale Ridgecrest Music Festival 2016</title>
<link href="https://fonts.googleapis.com/css2?family=Oswald:wght@300;400;500&display=swap" rel="stylesheet">
<style>
  :root {
    --backdrop: #1f2622;
    --sky-top: #b9d7db;
    --sky-mid: #6f98a3;
    --sky-low: #5f8792;
    --dusk: #4c5f78;
    --horizon: #8a6a7a;
    --water: #2f5d78;
    --water-deep: #3b6d88;
    --ink: #1b1f24;
    --festival: #5b3766;
    --band-light: rgba(235, 243, 245, 0.85);
    --genre-band: #4e4a2e;
    --accent-blue: #3aa0d0;
    --cream: #f1ead0;
    --web-text: #e8f0f2;
    --rule: rgba(255, 255, 255, 0.75);
  }
  html, body {
    margin: 0;
    width: 992px;
    height: 1200px;
    overflow: hidden;
    background: var(--backdrop);
  }
  .poster {
    position: absolute;
    left: 117px;
    top: 10px;
    width: 758px;
    height: 1180px;
    overflow: hidden;
    font-family: "Oswald", sans-serif;
    text-align: center;
    background: linear-gradient(180deg, var(--water) 0%, var(--water-deep) 100%);
  }
  .poster__sky {
    position: absolute;
    left: 0;
    top: 0;
    width: 100%;
    height: 425px;
    background: linear-gradient(180deg, var(--sky-top) 0%, #9cc2c9 45%, var(--sky-mid) 80%, var(--sky-low) 100%);
  }
  .poster__photo {
    position: absolute;
    left: 0;
    top: 473px;
    width: 100%;
    height: 433px;
    background: linear-gradient(180deg, var(--sky-low) 0%, var(--dusk) 35%, var(--horizon) 65%, #5a5d72 85%, var(--dusk) 100%);
  }
  .rule {
    position: absolute;
    left: 90px;
    width: 578px;
    height: 3px;
    background: var(--rule);
  }
  .rule--top { top: 88px; }
  .rule--bottom { top: 240px; }
  .festival-name {
    position: absolute;
    top: 104px;
    left: 0;
    width: 100%;
    margin: 0;
    font-weight: 400;
    font-size: 76px;
    line-height: 120px;
    letter-spacing: 1px;
    color: var(--ink);
  }
  .festival-sub {
    position: absolute;
    top: 252px;
    left: 0;
    width: 100%;
    margin: 0;
    font-weight: 300;
    font-size: 62px;
    line-height: 76px;
    letter-spacing: 2px;
    color: var(--festival);
  }
  .dates {
    position: absolute;
    top: 425px;
    left: 0;
    width: 100%;
    height: 48px;
    background: var(--band-light);
    color: #33383d;
    font-weight: 500;
    font-size: 29px;
    line-height: 48px;
    letter-spacing: 4px;
  }
  .year {
    position: absolute;
    top: 530px;
    left: 0;
    width: 100%;
    margin: 0;
    font-weight: 400;
    font-size: 290px;
    line-height: 340px;
    color: #1a2130;
    -webkit-text-stroke: 3px rgba(200, 225, 235, 0.85);
    text-shadow: 0 0 14px rgba(120, 190, 230, 0.5);
  }
  .genres {
    position: absolute;
    top: 906px;
    left: 0;
    width: 100%;
    height: 130px;
    background: linear-gradient(180deg, #5b5535, var(--genre-band) 60%, #3f4d48);
    border-top: 5px solid var(--accent-blue);
    border-bottom: 5px solid var(--accent-blue);
    box-sizing: border-box;
    padding-top: 8px;
  }
  .genres__line {
    margin: 0;
    color: var(--cream);
    font-weight: 400;
    font-size: 41px;
    line-height: 54px;
    letter-spacing: 1px;
  }
  .website {
    position: absolute;
    top: 1062px;
    left: 0;
    width: 100%;
    margin: 0;
    color: var(--web-text);
    font-weight: 400;
    font-size: 29px;
    letter-spacing: 3px;
  }
</style>
</head>
<body>
  <main class="poster">
    <div class="poster__sky" role="img" aria-label="Stock photograph of a pale teal sky with soft clouds"></div>
    <div class="poster__photo" role="img" aria-label="Stock photograph of two silhouetted musicians, one with a trumpet, against a dusk sky over a lake"></div>

    <div class="rule rule--top"></div>
    <h1 class="festival-name">FERN VALE RIDGECREST</h1>
    <div class="rule rule--bottom"></div>
    <p class="festival-sub">MUSIC FESTIVAL</p>

    <div class="dates">JULY 29 - AUGUST 7</div>

    <p class="year">2016</p>

    <div class="genres">
      <p class="genres__line">JAZZ | CHORAL | CABARET | EDUCATION</p>
      <p class="genres__line">BROADWAY | CHAMBER | OPERA</p>
    </div>

    <p class="website">WWW.FERNVALERIDGECRESTFEST.ORG</p>
  </main>
</body>
</html>
```